VORELA poster design that will include information about our project / product

We need a nice design for our poster (VORELA project poster). The content is presented in the attached doc file. With yellow are some instructions. We need a professional design for a European Project. <br/>I attach the logos of the Consortium that should be placed in the right order inside the Poster at the appropriate section (I attach the photos in different formats - you can use whichever logo is more convenient). I also attach the high-quality logo of VORELA.

Target Market(s)

Policy Makers, Health professionals

Industry/Entity Type

Health And Wellness

Font styles to use
Serif
Sans Serif

Colors
2f74b4
0255a3
33a6d7
ffcf3e
ffc214

Requirements
Must have
• - professional design
• - modern design
• - colors relevant to the logo
Nice to have
• Proposed size 80cm wide to 200cm height.

```html
<!DOCTYPE html>
<html lang="en">
<head>
<meta charset="utf-8">
<title>VORELA Project Poster</title>
<link rel="stylesheet" href="https://fonts.googleapis.com/css2?family=Poppins:wght@300;400&family=Roboto+Slab:wght@800&family=Sansita:wght@700&family=Fira+Sans:wght@500;600&family=PT+Sans+Narrow&display=swap">
<style>
:root{
  --stage:#e9e9ea;
  --sky:#33a6d7;
  --sun:#ffcf3e;
  --indigo:#4a5aa6;
  --ink-indigo:#3d4f9e;
  --card-grey:#e6e6e6;
  --white:#ffffff;
  --ink:#141414;
}
*{margin:0;padding:0;box-sizing:border-box}
html,body{width:1200px;height:1200px;overflow:hidden;background:var(--stage)}
.poster{position:absolute;left:207px;top:42px;width:786px;height:1158px;background:var(--sky);overflow:hidden}
.abs{position:absolute}
.header-art{position:absolute;left:0;top:0;width:786px;height:380px}
.ghost-mark{position:absolute;left:32px;top:-36px;width:254px;height:254px;border-radius:50%;border:3px solid rgba(170,170,175,.45)}
.ghost-name{position:absolute;left:32px;top:58px;width:254px;text-align:center;font-family:'Fira Sans',sans-serif;font-weight:500;font-size:52px;letter-spacing:6px;color:rgba(165,165,170,.45)}
.brand-badge{position:absolute;left:326px;top:25px;width:124px;height:124px;border-radius:50%;background:var(--indigo);display:flex;align-items:center;justify-content:center;font-family:'Fira Sans',sans-serif;font-weight:500;font-size:26px;letter-spacing:2px;color:var(--white)}
.project-title{position:absolute;left:176px;top:156px;width:420px;text-align:center;font-family:'Sansita',sans-serif;font-weight:700;font-size:22px;line-height:31px;letter-spacing:.3px;color:var(--white);text-shadow:0 0 2px #555,1px 1px 1px #444}
.section-title{position:absolute;left:54px;top:346px;font-family:'Roboto Slab',serif;font-weight:800;font-size:22px;line-height:28px;color:var(--white)}
.rationale{position:absolute;left:54px;top:373px;width:678px;font-family:'Poppins',sans-serif;font-weight:300;font-size:15.2px;line-height:20px;color:var(--white);text-align:justify}
.rationale p{margin-bottom:17px}
.dss-mark{position:absolute;left:321px;top:662px;width:66px;height:66px;border-radius:50%;border:2px solid var(--white);display:flex;align-items:center;justify-content:center;font-family:'Fira Sans',sans-serif;font-weight:500;font-size:13px;letter-spacing:1px;color:var(--white)}
.dss-label{position:absolute;left:396px;top:665px;font-family:'Fira Sans',sans-serif;font-weight:600;font-size:17px;line-height:20px;color:var(--white)}
.flow-accent{position:absolute;left:138px;top:754px;width:525px;height:267px;background:var(--sun)}
.flow-panel{position:absolute;left:129px;top:762px;width:525px;height:267px;background:var(--white)}
.col-title{position:absolute;font-family:'Roboto Slab',serif;font-weight:800;font-size:22px;line-height:26px;color:var(--ink-indigo);transform:translateX(-50%)}
.input-item{position:absolute;left:172px;display:flex;align-items:center;gap:5px;font-family:'PT Sans Narrow',sans-serif;font-size:14.5px;color:var(--ink-indigo);line-height:16px}
.input-item svg{width:20px;height:20px;flex:none}
.dss-card{position:absolute;left:327px;top:809px;width:129px;height:181px;border-radius:4px;background:var(--card-grey);overflow:hidden}
.dss-card-top{position:absolute;left:0;top:0;width:129px;height:70px;background:var(--sun);text-align:center}
.dss-hanger{position:absolute;left:380px;top:784px;width:25px;height:40px;border-radius:12px 12px 3px 3px;background:#dedede;border:2px solid #fff}
.dss-title{display:block;margin-top:22px;font-family:'Roboto Slab',serif;font-weight:800;font-size:26px;line-height:28px;color:var(--sky)}
.dss-sub{display:block;font-family:'Fira Sans',sans-serif;font-weight:500;font-size:12px;line-height:14px;color:#333}
.dss-rows{position:absolute;left:20px;top:82px}
.model-btn{position:absolute;left:15px;top:137px;width:99px;height:36px;border-radius:6px;background:var(--sky);color:var(--white);font-family:'Fira Sans',sans-serif;font-weight:500;font-size:12px;display:flex;align-items:center;justify-content:center}
.out-caption{position:absolute;left:463px;width:180px;text-align:center;font-family:'Fira Sans',sans-serif;font-size:11px;color:var(--ink-indigo)}
.out-strong{position:absolute;left:443px;width:196px;text-align:center;font-family:'Fira Sans',sans-serif;font-weight:600;font-size:16.5px;color:var(--ink-indigo)}
.scope-list{position:absolute;left:148px;top:1037px;width:520px;font-family:'PT Sans Narrow',sans-serif;font-size:16.5px;line-height:20px;color:var(--ink);list-style:none}
.scope-list li{position:relative;padding-left:10px;margin-bottom:10px}
.scope-list li::before{content:"•";position:absolute;left:0;font-size:11px}
</style>
</head>
<body>
<main class="poster">
  <svg class="header-art" viewBox="0 0 786 380" role="img" aria-label="Photograph of a man cupping his hand behind his ear to listen">
    <defs>
      <linearGradient id="photoTone" x1="0" y1="0" x2="1" y2="0">
        <stop offset="0" stop-color="#f3f4f6"/>
        <stop offset=".38" stop-color="#eae8e8"/>
        <stop offset=".55" stop-color="#e3b7a0"/>
        <stop offset=".8" stop-color="#d9977a"/>
        <stop offset="1" stop-color="#8d6b58"/>
      </linearGradient>
    </defs>
    <rect width="786" height="380" fill="url(#photoTone)"/>
    <path d="M0 110 C200 258 440 336 600 331 C690 328 750 314 786 298 L786 380 L0 380 Z" fill="#33a6d7"/>
    <path d="M0 110 C200 258 440 336 600 331 C690 328 750 314 786 298" fill="none" stroke="#ffcf3e" stroke-width="3"/>
  </svg>
  <div class="ghost-mark"></div>
  <div class="ghost-name">VORELA</div>
  <div class="brand-badge">VORELA</div>
  <h1 class="project-title">Validated Options for Remedies and Evaluation in Listening Ailments</h1>

  <h2 class="section-title">Rationale and Objectives</h2>
  <div class="rationale">
    <p>Tinnitus consists of the perception of a phantom sound including the patient’s reaction to it. Tinnitus remains a scientific and clinical enigma of immensely high prevalence and socio-economic burden.</p>
    <p>The overall aim of the VORELA project is to deliver a predictive computational model based on existing and longitudinal data attempting to address the question, which tinnitus treatment approach is optimal for a specific patient group based on specific parameters.</p>
    <p>Clinical, epidemiological, medical, genetic and audiological data, including signals reflecting ear-brain communication, will be analysed from existing databases. Predictive factors for different patient groups will be extracted and their prognostic relevance will be validated in a randomized controlled trial (RCT) in which different groups of patients will undergo a combination of therapies targeting both auditory and central nervous.</p>
  </div>

  <div class="dss-mark">VORELA</div>
  <div class="dss-label">Decision<br>Support<br>System</div>

  <div class="flow-accent"></div>
  <div class="flow-panel"></div>

  <div class="col-title" style="left:223px;top:784px">Input</div>
  <div class="input-item" style="top:817px"><svg viewBox="0 0 20 20" fill="none" stroke="#3d4f9e" stroke-width="1.3"><path d="M3 18 C8 14 12 8 17 2M6 18 C6 12 12 8 17 6"/><path d="M6 15l3 1M9 11l3 1M12 7l3 1"/></svg>Genetic data</div>
  <div class="input-item" style="top:851px"><svg viewBox="0 0 20 20" fill="none" stroke="#3d4f9e" stroke-width="1.3"><path d="M1 11h5l2-6 3 11 2-5h6"/></svg>Electrophysiological data</div>
  <div class="input-item" style="top:886px"><svg viewBox="0 0 20 20" fill="none" stroke="#3d4f9e" stroke-width="1.3"><path d="M4 7a4 4 0 0 1 8 0c0 3-3 4-3 7a2 2 0 0 1-4 0"/><path d="M14 5q2 4 0 8M16 3q3 6 0 12"/></svg>Tinnitus characteristics</div>
  <div class="input-item" style="top:920px"><svg viewBox="0 0 20 20" fill="none" stroke="#3d4f9e" stroke-width="1.2"><rect x="4" y="3" width="12" height="15" rx="1"/><path d="M8 2h4v2H8zM7 8h6M7 11h6M7 14h4"/></svg>Medical history</div>
  <div class="input-item" style="top:955px"><svg viewBox="0 0 20 20" fill="#3d4f9e"><circle cx="5" cy="8" r="2.5"/><circle cx="10" cy="6" r="2.5"/><circle cx="15" cy="8" r="2.5"/><path d="M1 16a4 4 0 0 1 8 0zM6 15a4 4 0 0 1 8 0zM11 16a4 4 0 0 1 8 0z"/></svg>Epidemiological</div>
  <div class="input-item" style="top:990px"><svg viewBox="0 0 20 20" fill="none" stroke="#3d4f9e" stroke-width="1.2"><rect x="3" y="4" width="12" height="14" rx="1"/><path d="M7 3h4v2H7zM6 9h6M6 12h4M10 16l7-7 1 1-7 7h-1z"/></svg>Questionnaires</div>

  <div class="dss-hanger"></div>
  <div class="dss-card">
    <div class="dss-card-top">
      <span class="dss-title">DSS</span>
      <span class="dss-sub">Feature extraction</span>
    </div>
    <svg class="dss-rows" width="70" height="50" viewBox="0 0 70 50" fill="#444">
      <circle cx="7" cy="5" r="4.5"/><path d="M0 18a7 6 0 0 1 14 0z"/>
      <rect x="22" y="3" width="18" height="2.5"/><rect x="22" y="9" width="12" height="2.5"/><rect x="22" y="15" width="16" height="2.5"/>
      <circle cx="7" cy="31" r="4.5"/><path d="M0 45a7 6 0 0 1 14 0z"/>
      <rect x="22" y="30" width="18" height="2.5"/><rect x="22" y="37" width="12" height="2.5"/>
    </svg>
    <div class="model-btn">In-silico model</div>
  </div>

  <div class="col-title" style="left:537px;top:784px">Output</div>
  <svg class="abs" style="left:508px;top:834px" width="92" height="42" viewBox="0 0 92 42">
    <g fill="none" stroke="#3d4f9e" stroke-width="2.2"><path d="M2 9V3h6M34 3h6v6M40 31v6h-6M8 37H2v-6"/></g>
    <circle cx="21" cy="14" r="6" fill="#3d4f9e"/><path d="M10 32a11 9 0 0 1 22 0z" fill="#3d4f9e"/>
    <circle cx="70" cy="20" r="19" fill="none" stroke="#3d4f9e" stroke-width="1.6"/>
    <g fill="none" stroke="#3d4f9e" stroke-width="1.3"><rect x="63" y="11" width="14" height="18"/><path d="M66 16h8M66 19h8M66 22h8M66 25h8"/></g>
  </svg>
  <div class="out-caption" style="top:882px">Personalised set of examinations</div>
  <svg class="abs" style="left:521px;top:912px" width="40" height="36" viewBox="0 0 40 36" fill="#3d4f9e">
    <rect x="17" y="0" width="5" height="17"/><rect x="11" y="6" width="17" height="5"/>
    <path d="M1 26 C10 22 16 22 22 25 L30 25 C33 25 33 28 30 28 L20 28 L30 29 L38 25 C40 25 40 28 38 29 L28 34 L12 33 L1 32 Z"/>
  </svg>
  <div class="out-strong" style="top:952px">Optimal treatment</div>

  <ul class="scope-list">
    <li>Patient 1, Patient 2, Patient 3, ....., Patient 70.000.000;</li>
    <li>Treatment 1, Treatment 2, Treatment 3, Treatment 4, ..., T1+T2, T1+T3, T1+T4, ..., T2+T3, T2+T4, ..., T1+T2+T3, T1+T2+T4, ...;</li>
  </ul>
</main>
</body>
</html>
```